Beef cattle farm needs signs which can be seen from roadside

We would like submissions of artwork for a sign that will hang from a fence or gate and will be seen by passing cars.

Existing logo and branding theme for the company is attached.

Signage can be between 900mm x 400mm - 1200mm x 600mm

Industry/Entity Type

Farm

Requirements
Must have
• the Signs should have the following information:
• Company name: Brindle Ridge Grazing Company
• Address: 214 Wattlebank Hollow Road
• Contact number: 0431 862 475
• email address: admin@brindleridgegrazingco.com.au
• - Logo and branding as per attached artwork

```html
<!DOCTYPE html>
<html lang="en">
<head>
<meta charset="utf-8">
<title>Brindle Ridge Grazing Company – Roadside Sign</title>
<link rel="stylesheet" href="https://fonts.googleapis.com/css2?family=Montserrat:wght@400;700;800&display=swap">
<style>
  :root {
    --green-light: #56ae3b;
    --green-dark: #2c6940;
    --pill-green: #5cb244;
    --phone-green: #3f8f3a;
    --ink: #1f1f1f;
    --white: #ffffff;
    --band-grey: #e6e6e6;
    --band-pale: #f7f7f7;
  }
  html, body {
    margin: 0;
    padding: 0;
    width: 1200px;
    height: 629px;
    overflow: hidden;
    background: var(--white);
  }
  .sign {
    position: relative;
    width: 1200px;
    height: 629px;
    background: var(--white);
    font-family: "Montserrat", Arial, sans-serif;
  }
  .sign__panel {
    position: absolute;
    left: 29px;
    top: 29px;
    width: 1142px;
    height: 449px;
    background: linear-gradient(90deg, var(--green-light) 0%, #3f8a3c 50%, var(--green-dark) 100%);
  }
  .sign__emblem {
    position: absolute;
    left: 55px;
    top: 51px;
    width: 320px;
    height: 320px;
    border-radius: 50%;
    background: var(--white);
  }
  .sign__name {
    position: absolute;
    left: 462px;
    top: 110px;
    width: 680px;
    height: 240px;
  }
  .sign__name text {
    fill: var(--white);
    font-family: "Montserrat", Arial, sans-serif;
    font-weight: 700;
  }
  .sign__email {
    position: absolute;
    left: 468px;
    top: 376px;
    width: 532px;
    height: 52px;
    border-radius: 8px;
    background: linear-gradient(90deg, var(--pill-green) 0%, rgba(92,178,68,0.55) 70%, rgba(92,178,68,0) 100%);
    color: var(--white);
    font-size: 24px;
    font-weight: 400;
    line-height: 52px;
    padding-left: 16px;
    box-sizing: border-box;
    white-space: nowrap;
  }
  .sign__contact-band {
    position: absolute;
    left: 29px;
    top: 478px;
    width: 1142px;
    height: 95px;
    overflow: hidden;
    background: linear-gradient(90deg, var(--band-grey) 0%, var(--band-pale) 50%, var(--band-grey) 100%);
  }
  .sign__phone,
  .sign__address {
    position: absolute;
    top: 0;
    line-height: 95px;
    font-weight: 700;
    white-space: nowrap;
  }
  .sign__phone {
    left: 53px;
    font-size: 46px;
    color: var(--phone-green);
  }
  .sign__address {
    left: 441px;
    font-size: 41px;
    color: var(--ink);
  }
  .sign__base-stripe {
    position: absolute;
    left: 29px;
    top: 573px;
    width: 1142px;
    height: 27px;
    background: linear-gradient(90deg, var(--green-light) 0%, #3f8a3c 50%, var(--green-dark) 100%);
  }
</style>
</head>
<body>
<main class="sign">
  <section class="sign__panel">
    <div class="sign__emblem" aria-hidden="true"></div>
  </section>

  <svg class="sign__name" viewBox="0 0 680 240" role="heading" aria-level="1" aria-label="Brindle Ridge Grazing Company">
    <text x="6" y="118" font-size="92" textLength="648" lengthAdjust="spacingAndGlyphs">BRINDLE RIDGE</text>
    <text x="6" y="222" font-size="60" textLength="648" lengthAdjust="spacingAndGlyphs">GRAZING COMPANY</text>
  </svg>

  <div class="sign__email">admin@brindleridgegrazingco.com.au</div>

  <section class="sign__contact-band">
    <div class="sign__phone">0431 862 475</div>
    <div class="sign__address">214 Wattlebank Hollow Road</div>
  </section>

  <div class="sign__base-stripe"></div>
</main>
</body>
</html>
```